Wollondilly ridge aerial works business card size advertising

I’m after a simple design , please see attached photo . Im after the same color green in the photo as the base color and the the little white man but instead of him holding a spanner i would like him to be holding a tv antenna pointing an angle , see attached photo of the antenna , i would like him on the left of the business card and the business name to fit in on the right with the phone number . ( if the antenna idea looks stupid , leave him holding a spanner ) On the reverse side of the card i would like a white background with green writing stating some of the services we provide which are the following .Antenna installations and repairs Wall mounting of tv’s Additional TV outlets Brolga satellite supply and installations Goulburn , Crookwell , Taralga , Tarago , Marulan , Collector , All rural areas All in all i would like the business card to compliment my invoices as pictured “ invoice supplied is a dummy invoice “

Contact Information for Business Card

wollondilly ridge aerial works 0418563927

Font styles to use
Sans Serif

Colors
9bcb3c

Requirements
Must have
• what i ask for in project description

```html
<!DOCTYPE html>
<html lang="en">
<head>
<meta charset="utf-8">
<title>Wollondilly Ridge Aerial Works – Business Card</title>
<link rel="stylesheet" href="https://fonts.googleapis.com/css2?family=Montserrat:wght@500;600;700&display=swap">
<style>
  :root {
    --green: #74c388;
    --ink: #414141;
    --paper: #ffffff;
    --backdrop: #e9ebea;
  }
  * { box-sizing: border-box; margin: 0; padding: 0; }
  html, body { width: 1200px; height: 1000px; overflow: hidden; }
  body {
    background: var(--backdrop);
    font-family: "Montserrat", sans-serif;
    position: relative;
  }
  .card {
    position: absolute;
    left: 250px;
    width: 700px;
    height: 400px;
    background: var(--paper);
    border-radius: 22px;
    overflow: hidden;
    box-shadow: 0 6px 22px rgba(0,0,0,0.12);
  }
  .card--front { top: 50px; }
  .card--back { top: 530px; }

  .figure-art {
    position: absolute;
    left: 45px;
    top: 70px;
    width: 150px;
    height: 220px;
    background: var(--green);
    border-radius: 6px;
  }
  .brand {
    position: absolute;
    left: 222px;
    top: 135px;
    right: 30px;
  }
  .brand__name {
    color: var(--ink);
    font-weight: 700;
    font-size: 33px;
    line-height: 1.02;
    text-transform: uppercase;
    letter-spacing: 0.5px;
    white-space: nowrap;
  }
  .brand__phone {
    color: var(--green);
    font-weight: 600;
    font-size: 64px;
    line-height: 1.1;
    letter-spacing: 0.5px;
    margin-top: 4px;
    margin-left: -3px;
    white-space: nowrap;
  }

  .services-band {
    position: absolute;
    left: 0; right: 0;
    top: 56px;
    height: 58px;
    background: var(--green);
    color: var(--paper);
    font-weight: 700;
    font-size: 30px;
    letter-spacing: 1.5px;
    text-align: center;
    line-height: 58px;
    text-transform: uppercase;
  }
  .services-list {
    position: absolute;
    left: 0; right: 0;
    top: 124px;
    list-style: none;
    text-align: center;
    color: var(--green);
    font-weight: 700;
    font-size: 23px;
    line-height: 1.2;
    letter-spacing: 1px;
    text-transform: uppercase;
  }
  .call-line {
    position: absolute;
    left: 0; right: 0;
    top: 254px;
    text-align: center;
    color: var(--green);
    font-weight: 700;
    font-size: 31px;
    letter-spacing: 1.5px;
    text-transform: uppercase;
  }
  .area-band {
    position: absolute;
    left: 0; right: 0;
    bottom: 0;
    height: 50px;
    background: var(--green);
    color: var(--paper);
    font-weight: 500;
    font-size: 16.5px;
    line-height: 50px;
    text-align: center;
    letter-spacing: 0;
    white-space: nowrap;
  }
</style>
</head>
<body>
  <section class="card card--front">
    <div class="figure-art" role="img" aria-label="Green flat illustration of a worker in a cap holding a TV antenna at an angle"></div>
    <div class="brand">
      <p class="brand__name">Wollondilly Ridge<br>Aerial Works</p>
      <p class="brand__phone">0418563927</p>
    </div>
  </section>

  <section class="card card--back">
    <h2 class="services-band">Services we provide</h2>
    <ul class="services-list">
      <li>Antenna installations and repairs</li>
      <li>Wall mounting of TV’s</li>
      <li>Additional TV outlets</li>
      <li>Brolga satellite supply and installations</li>
    </ul>
    <p class="call-line">Call Callum : 0418563927</p>
    <p class="area-band">Goulburn | Crookwell | Taralga | Tarago | Marulan | Collector | All rural areas</p>
  </section>
</body>
</html>
```